KWT Contracting services . Building and maintenance services, optic fibre installation

Business cards and logo design.I need a logo that I can use on business cards ,workwear and on my vehicles. I would like the KWT to be the main or larger text and contracting services to be the smaller or less important text.I like monograms, modern designs and repeating patterns symbols. I am also a Gemini and my favourite number is 22 so if this can be any inspiration to help with the design. Am thinking of the using German flag colours as a his is my family’s heritage. And the other 2 main colours I wear is black and white.But any ideas are appreciated.I do not need a design that is trade specific but a design that could be used for any business.

Target Market(s)

General public

Contact Information for Business Card

KWT Contracting Services ( front of business card)

(Back of business card)
Milo Brackwood
0471539264
Maintenance services
Optic fibre and data installation

Logo Text

Logo can just be pattern or monogram or incorporate KWT . I like the gemini star sign and the number 22

Colors
ec1f27
000000
fbee3e
ffffff

Requirements
Must have
• Logo and KWT Contracting Services on the front of business card
Nice to have
• Possible use of German flag colours.
• Modern design.
• Design to be able to be used on black or white background as I want to put it on clothing

```html
<!DOCTYPE html>
<html lang="en">
<head>
<meta charset="utf-8">
<title>KWT Contracting Services – Business Card</title>
<link href="https://fonts.googleapis.com/css2?family=Cinzel:wght@400;600&family=Exo+2:wght@400&display=swap" rel="stylesheet">
<style>
  :root {
    --ink: #000000;
    --card-dark: #141414;
    --card-dark-edge: #050505;
    --card-dark-glow: #2a2a2a;
    --paper: #ffffff;
    --red: #ec1f27;
    --red-deep: #a8121a;
    --gold: #c9a43a;
    --gold-light: #f0d77a;
    --silver: #c9c9c9;
    --stage: #e9e7e3;
    --card-w: 540px;
    --card-h: 309px;
  }
  * { box-sizing: border-box; margin: 0; padding: 0; }
  html, body {
    width: 1200px;
    height: 800px;
    overflow: hidden;
    background: var(--stage);
  }
  .sheet {
    width: 1200px;
    height: 800px;
    display: flex;
    align-items: center;
    justify-content: center;
    gap: 40px;
  }
  .card {
    position: relative;
    width: var(--card-w);
    height: var(--card-h);
    overflow: hidden;
    box-shadow: 0 10px 28px rgba(0,0,0,0.25);
  }

  /* Front */
  .card--front {
    background: radial-gradient(ellipse at 50% 45%, var(--card-dark-glow) 0%, var(--card-dark) 45%, var(--card-dark-edge) 100%);
  }
  .card--front .backdrop {
    position: absolute;
    inset: 0;
    background: radial-gradient(circle at 50% 40%, rgba(255,255,255,0.05) 0%, rgba(255,255,255,0) 60%);
  }
  .brand {
    position: absolute;
    display: flex;
    flex-direction: column;
    align-items: center;
    font-family: "Cinzel", serif;
  }
  .card--front .brand {
    left: 0; right: 0; top: 62px;
  }
  .brand__mark {
    display: flex;
    align-items: center;
    gap: 12px;
    color: var(--gold);
    font-weight: 600;
    line-height: 1;
  }
  .brand__dot {
    border-radius: 50%;
    background: var(--red);
  }
  .card--front .brand__mark { font-size: 80px; }
  .card--front .brand__dot { width: 16px; height: 16px; }
  .brand__name {
    color: var(--silver);
    font-weight: 400;
    line-height: 1.1;
    margin-top: 12px;
  }
  .card--front .brand__name { font-size: 28px; }
  .brand__sub {
    display: flex;
    align-items: center;
    gap: 8px;
    color: var(--silver);
    font-weight: 400;
    letter-spacing: 0.08em;
  }
  .card--front .brand__sub { font-size: 21px; margin-top: 2px; }
  .brand__rule {
    height: 1px;
    background: var(--silver);
    opacity: 0.7;
  }
  .card--front .brand__rule { width: 46px; }

  /* Back */
  .card--back { background: var(--paper); }
  .card--back .wave {
    position: absolute;
    inset: 0;
    width: 100%;
    height: 100%;
  }
  .card--back .brand {
    left: 0; width: 300px; top: 72px;
  }
  .card--back .brand__mark { font-size: 62px; }
  .card--back .brand__dot { width: 13px; height: 13px; }
  .card--back .brand__name { font-size: 22px; margin-top: 10px; }
  .card--back .brand__sub { font-size: 16px; }
  .card--back .brand__rule { width: 36px; }

  .contact {
    position: absolute;
    right: 28px;
    top: 86px;
    width: 220px;
    font-family: "Exo 2", sans-serif;
    color: var(--ink);
  }
  .contact__name {
    color: var(--red);
    font-size: 18px;
    line-height: 1.2;
  }
  .contact__phone {
    font-size: 19px;
    letter-spacing: 0.02em;
    line-height: 1.3;
    margin-left: 10px;
  }
  .contact__services {
    list-style: none;
    margin-top: 26px;
    text-align: right;
    font-size: 14px;
    line-height: 1.45;
  }
</style>
</head>
<body>
<main class="sheet">

  <section class="card card--front" aria-label="Business card front">
    <div class="backdrop"></div>
    <div class="brand">
      <div class="brand__mark"><span class="brand__dot"></span>KWT</div>
      <div class="brand__name">KWT Contracting</div>
      <div class="brand__sub"><span class="brand__rule"></span>services<span class="brand__rule"></span></div>
    </div>
  </section>

  <section class="card card--back" aria-label="Business card back">
    <svg class="wave" viewBox="0 0 540 309" preserveAspectRatio="none" aria-hidden="true">
      <defs>
        <radialGradient id="darkPanel" cx="0.35" cy="0.45" r="0.75">
          <stop offset="0" stop-color="#2a2a2a"/>
          <stop offset="0.5" stop-color="#141414"/>
          <stop offset="1" stop-color="#050505"/>
        </radialGradient>
        <linearGradient id="redBand" x1="0" y1="0" x2="0" y2="1">
          <stop offset="0" stop-color="#ec1f27"/>
          <stop offset="1" stop-color="#a8121a"/>
        </linearGradient>
        <linearGradient id="goldLine" x1="0" y1="0" x2="0" y2="1">
          <stop offset="0" stop-color="#f0d77a"/>
          <stop offset="1" stop-color="#c9a43a"/>
        </linearGradient>
      </defs>
      <path d="M0 0 H362 C300 50 262 140 266 220 C268 262 280 290 292 309 H0 Z" fill="url(#darkPanel)"/>
      <path d="M310 112 C278 160 266 232 300 309 H284 C254 240 266 168 310 112 Z" fill="url(#redBand)"/>
      <path d="M318 124 C292 172 284 236 312 309 H306 C276 240 284 176 318 124 Z" fill="url(#goldLine)"/>
    </svg>
    <div class="brand">
      <div class="brand__mark"><span class="brand__dot"></span>KWT</div>
      <div class="brand__name">KWT Contracting</div>
      <div class="brand__sub"><span class="brand__rule"></span>services<span class="brand__rule"></span></div>
    </div>
    <div class="contact">
      <p class="contact__name">Milo Brackwood</p>
      <p class="contact__phone">0471539264</p>
      <ul class="contact__services">
        <li>Maintenance services</li>
        <li>Optic fibre and data installation</li>
      </ul>
    </div>
  </section>

</main>
</body>
</html>
```